Album/CD/Online Cover Art.

Music Album cover art for online distribution. Art should be .jpg file format, perfectly square, and 3000x3000 pixels. Band Name: Heron Velvet. Album Name: One Truly Velvet Lantern Night.
White background, with a very simple christmas theme. Include a falcon with a santa hat on. I’ve had several album covers done through pixel bazaar, let me know if you cant see them and I’ll send them for reference.

```html
<!DOCTYPE html>
<html lang="en">
<head>
<meta charset="utf-8">
<title>Heron Velvet – One Truly Velvet Lantern Night</title>
<link rel="stylesheet" href="https://fonts.googleapis.com/css2?family=Anton&family=Cormorant+Garamond:wght@600&display=swap">
<style>
  :root {
    --backdrop: #5a5a5a;
    --paper: #ffffff;
    --pine: #0f6b35;
    --berry: #d4171f;
    --hole: #5a5a5a;
    --plumage-light: #c9a582;
    --plumage-dark: #6e5640;
    --holly: #2f6b2a;
  }
  html, body {
    margin: 0;
    padding: 0;
    width: 992px;
    height: 1200px;
    overflow: hidden;
    background: var(--backdrop);
  }
  .canvas {
    position: relative;
    width: 992px;
    height: 1200px;
  }
  .album-cover {
    position: absolute;
    left: 216px;
    top: 50px;
    width: 560px;
    height: 560px;
    background: var(--paper);
  }
  .disc-label {
    position: absolute;
    left: 236px;
    top: 650px;
    width: 520px;
    height: 520px;
  }
  .band-name {
    font-family: "Anton", "Oswald", sans-serif;
    fill: var(--pine);
  }
  .band-echo {
    font-family: "Anton", "Oswald", sans-serif;
    fill: none;
    stroke: var(--pine);
    stroke-width: 0.8;
  }
  .album-title {
    font-family: "Cormorant Garamond", "Times New Roman", serif;
    font-weight: 600;
    fill: var(--berry);
  }
</style>
</head>
<body>
<main class="canvas">

  <svg class="album-cover" viewBox="0 0 560 560" xmlns="http://www.w3.org/2000/svg">
    <defs>
      <linearGradient id="plumage" x1="0" y1="0" x2="0" y2="1">
        <stop offset="0" stop-color="#d6232a"/>
        <stop offset="0.16" stop-color="#f2efe9"/>
        <stop offset="0.3" stop-color="var(--plumage-light)"/>
        <stop offset="1" stop-color="var(--plumage-dark)"/>
      </linearGradient>
      <linearGradient id="foliage" x1="0" y1="0" x2="1" y2="1">
        <stop offset="0" stop-color="var(--holly)"/>
        <stop offset="1" stop-color="#b3262c"/>
      </linearGradient>
    </defs>
    <rect class="cover-ground" width="560" height="560" fill="var(--paper)"/>

    <text class="band-name" x="30" y="100" font-size="84" textLength="500" lengthAdjust="spacingAndGlyphs">HERON VELVET</text>
    <text class="band-echo" x="30" y="172" font-size="84" textLength="500" lengthAdjust="spacingAndGlyphs" opacity="0.55">HERON VELVET</text>
    <text class="band-echo" x="30" y="244" font-size="84" textLength="500" lengthAdjust="spacingAndGlyphs" opacity="0.35">HERON VELVET</text>
    <text class="band-echo" x="30" y="316" font-size="84" textLength="500" lengthAdjust="spacingAndGlyphs" opacity="0.2">HERON VELVET</text>
    <text class="band-echo" x="30" y="388" font-size="84" textLength="500" lengthAdjust="spacingAndGlyphs" opacity="0.08">HERON VELVET</text>

    <rect class="holly-sprig" x="145" y="312" width="80" height="52" rx="20" fill="url(#foliage)"
          role="img" aria-label="Holly leaves with red berries on the branch"/>
    <rect class="falcon-illustration" x="250" y="82" width="190" height="400" rx="80" fill="url(#plumage)"
          role="img" aria-label="Falcon wearing a Santa hat, perched on a branch"/>
    <rect class="branch" x="180" y="372" width="380" height="14" rx="7" fill="#7a5a42"
          role="img" aria-label="Bare tree branch"/>

    <text class="album-title" x="40" y="448" font-size="46">One Truly</text>
    <text class="album-title" x="32" y="508" font-size="50" textLength="498" lengthAdjust="spacingAndGlyphs">Velvet Lantern Night</text>
  </svg>

  <svg class="disc-label" viewBox="0 0 520 520" xmlns="http://www.w3.org/2000/svg">
    <defs>
      <path id="disc-arc" d="M 70 300 A 200 200 0 0 1 430 130"/>
      <linearGradient id="disc-plumage" x1="0" y1="0" x2="0" y2="1">
        <stop offset="0" stop-color="#d6232a"/>
        <stop offset="0.16" stop-color="#f2efe9"/>
        <stop offset="0.3" stop-color="var(--plumage-light)"/>
        <stop offset="1" stop-color="var(--plumage-dark)"/>
      </linearGradient>
    </defs>
    <circle class="disc-face" cx="260" cy="260" r="258" fill="var(--paper)"/>
    <circle class="disc-hole" cx="260" cy="260" r="56" fill="var(--hole)"/>

    <text class="band-name" font-size="44" letter-spacing="4">
      <textPath href="#disc-arc">HERON VELVET</textPath>
    </text>

    <rect class="falcon-illustration" x="370" y="150" width="110" height="240" rx="48" fill="url(#disc-plumage)"
          role="img" aria-label="Falcon wearing a Santa hat, perched on a holly branch"/>
    <rect class="branch" x="320" y="318" width="195" height="9" rx="4" fill="#7a5a42"
          role="img" aria-label="Bare tree branch with holly"/>

    <text class="album-title" x="80" y="355" font-size="42">One Truly</text>
    <text class="album-title" x="110" y="405" font-size="42">Velvet Lantern</text>
    <text class="album-title" x="160" y="455" font-size="42">Night</text>
  </svg>

</main>
</body>
</html>
```